Ferrowave.com website design

I need a basic website for www.ferrowave.com. Ferro Wave has been hosting websites since 2002 via partnership arrangement with Stackhollow.com and Namequarry.com. We do not do any design, only hosting for small companies and nonprofits. We are referring people to PixelGuild and others to get their websites developed. Our website and pricing does not change often, but I need to be able to easily update the pricing and contact page.

Target Market(s)

Small company and non profit organizations

Industry/Entity Type

Utility

Coding

Coded - Design and coding required

Number of Pages Required

5+ page

Colors

Designer to choose colors to be used in the design.

Requirements
Must have
• Wordsmith format for easy content management. The logo attached. Contact us page with the following: Phone and fax are the same number: 888.514.2973. Email address is myferrowave@mailnest.example. Mailing address is 4819 E. Tolliver Bend #317, Searcy, AR 72143.
Nice to have
• Some kind of badge or tag line on the home page that celebrates our 15th year of hosting without a single hosting without any downtime. We are are 15 year partners with Stackhollow.com and Namequarry.com. Website Design tab needs to reference PixelGuild or others for all their website design needs. We provide no design or updating services. We will provide the developers FTP access to our dedicated Linux server. We do not provide email services other than redirects to their proprietary email or gmail, yahoo, etc. Needs a services and pricing tab. We provide domain registration services via our partnership with Namequarry.com. We will want a way for them to submit a suggested domain name for us to verify if available. I might be able to get a link from Namequarry.com to our account for you to include on that tab REGISTER DOMAIN. The tab buttons can be: WHO WE ARE, WHAT WE DO, WHEN YOU NEED US, WHERE TO REACH US. Maybe consider making the WHO, WHAT, WHEN and WHERE a dark blue color the rest of the text different color just so they stand out
Should not have
• A lot of animation that takes a long time to open. Clean and simple website.

```html
<!DOCTYPE html>
<html lang="en">
<head>
<meta charset="utf-8">
<title>Ferro Wave – Web Hosting Services</title>
<link href="https://fonts.googleapis.com/css2?family=Open+Sans:wght@400;600;700&family=Roboto:wght@400;500;700;900&display=swap" rel="stylesheet">
<style>
:root{
  --orange:#f6a623;
  --orange-dark:#e58f12;
  --orange-light:#fbc25b;
  --teal:#1d8ea6;
  --navy:#16314b;
  --navy-deep:#0f2236;
  --navy-darkest:#0a1a2a;
  --blue:#3d8fd3;
  --pale:#e8f5fa;
  --card-body:#dff1f7;
  --yellow:#f7c430;
  --green-teal:#3ec2bd;
  --red:#ee6048;
  --text:#4a5866;
  --white:#ffffff;
}
*{box-sizing:border-box;margin:0;padding:0}
html,body{width:1200px;height:3312px;overflow:hidden}
body{font-family:"Open Sans",sans-serif;color:var(--text);background:var(--white);position:relative}
.abs{position:absolute}
h1,h2,h3,h4{font-family:"Roboto",sans-serif}

/* hero */
.hero{left:0;top:0;width:1200px;height:580px;background:linear-gradient(180deg,var(--orange-light),var(--orange) 70%)}
.brand{left:60px;top:18px;display:flex;align-items:center;gap:10px;color:var(--white);font-family:"Roboto",sans-serif;font-weight:700;font-size:20px;letter-spacing:1px}
.brand-mark{width:30px;height:30px;background:var(--teal)}
.main-nav{left:370px;top:40px;display:flex;gap:28px;font-family:"Roboto",sans-serif;font-size:12px;font-weight:500;color:var(--white);letter-spacing:.5px;white-space:nowrap}
.main-nav .wh{color:var(--navy);font-weight:700}
.badge{left:980px;top:110px;width:150px;height:200px;background:var(--teal);color:var(--white);font-family:"Roboto",sans-serif;text-align:center;padding-top:18px}
.badge .num{font-size:84px;font-weight:900;line-height:1}
.badge .yrs{font-size:26px;font-weight:500;margin-top:4px}
.badge .of{font-size:13px;margin-top:6px;letter-spacing:1px}
.hero-title{left:0;width:1200px;top:120px;text-align:center;color:var(--white);font-size:38px;font-weight:400}
.btn{display:inline-block;background:var(--orange-dark);color:var(--white);font-family:"Roboto",sans-serif;font-size:12px;font-weight:500;letter-spacing:.5px;text-align:center;border-radius:2px}
.hero-btn{left:548px;top:182px;width:104px;height:26px;line-height:26px;background:#d9820a}
.hero-art{left:350px;top:230px;width:500px;height:290px;border-radius:30px;background:radial-gradient(ellipse at center,#f4f1e8 0%,#f1c77c 60%,rgba(246,166,35,0) 75%)}
.torn{left:0;top:530px;width:1200px;height:60px}

/* about */
.about{left:0;top:580px;width:1200px;height:540px;background:var(--pale)}
.about h2{left:108px;top:44px;font-size:30px;color:var(--navy);font-weight:500}
.about-copy{left:108px;top:100px;width:470px;font-size:12.5px;line-height:1.6}
.about-copy p{margin-bottom:14px}
.learn{left:108px;top:390px;width:112px;height:38px;line-height:34px;border:2px solid var(--orange);color:var(--navy);font-family:"Roboto",sans-serif;font-weight:700;font-size:14px;text-align:center;background:var(--white)}
.about-art{left:700px;top:40px;width:320px;height:260px;border-radius:16px;background:radial-gradient(ellipse at center,#c9e4f2 0%,#e1f0f7 70%)}

/* domain */
.domain{left:0;top:1120px;width:1200px;height:80px;background:var(--navy)}
.domain-label{left:100px;top:14px;font-family:"Roboto",sans-serif;color:var(--white)}
.domain-label small{display:block;font-size:12px;letter-spacing:1px}
.domain-label b{display:block;color:var(--orange);font-size:30px;font-weight:700;line-height:1}
.domain-input{left:340px;top:24px;width:560px;height:32px;background:#e9eef3}
.domain-ext{left:900px;top:24px;width:60px;height:32px;background:#cfd8e0;font-size:11px;line-height:32px;text-align:center;color:var(--navy)}
.domain-btn{left:960px;top:24px;width:140px;height:32px;line-height:32px;background:var(--orange-dark);font-size:13px}

/* services */
.services{left:0;top:1200px;width:1200px;height:400px;background:linear-gradient(180deg,#4c9ee0,#2f7fc4)}
.section-title{width:1200px;left:0;text-align:center;font-weight:700;font-size:30px;letter-spacing:1px}
.services .section-title{top:56px;color:var(--white)}
.svc{top:140px;width:220px;text-align:center;color:var(--white)}
.svc svg{display:block;margin:0 auto 18px}
.svc h3{font-size:17px;font-weight:500;margin-bottom:8px}
.svc p{font-size:10.5px;line-height:1.5;opacity:.85;margin-bottom:16px}
.svc .btn{width:64px;height:20px;line-height:20px;font-size:10px;background:var(--orange)}

/* prices */
.prices{left:0;top:1600px;width:1200px;height:760px;background:#eef8fb}
.prices .section-title{top:60px;color:var(--navy)}
.prices-sub{left:400px;top:110px;width:400px;text-align:center;font-size:11px;line-height:1.5}
.plan{top:220px;width:312px;height:520px;background:var(--card-body);box-shadow:0 2px 6px rgba(0,0,0,.08)}
.plan-head{height:110px;text-align:center;padding-top:22px;color:var(--navy)}
.plan-head h3{font-size:34px;font-weight:500;letter-spacing:1px}
.plan-head p{font-size:12px;margin-top:4px}
.plan ul{list-style:none;padding:16px 28px 0}
.plan li{font-size:11px;font-weight:600;color:#55626f;padding:17px 0;border-bottom:1px solid #c5dde6;letter-spacing:.3px}
.plan .btn{display:block;width:96px;height:26px;line-height:26px;margin:26px auto 0;font-size:10px}
.plan.beginner .plan-head{background:var(--yellow)}
.plan.beginner .btn{background:var(--orange)}
.plan.standard .plan-head{background:var(--green-teal)}
.plan.standard .btn{background:var(--green-teal)}
.plan.establishment .plan-head{background:var(--red);color:var(--white)}
.plan.establishment .plan-head h3{color:var(--navy)}
.plan.establishment .btn{background:var(--red)}

/* testimonials */
.clients{left:0;top:2360px;width:1200px;height:480px;background:linear-gradient(180deg,#f8c46a 0%,#f5a623 55%,#e8931a 100%)}
.clients .section-title{top:40px;color:var(--navy);font-size:28px}
.avatar{left:540px;top:100px;width:120px;height:120px;border-radius:50%;background:#d8cdbf;border:4px solid var(--white)}
.client-name{left:0;width:1200px;top:236px;text-align:center;font-family:"Roboto",sans-serif;font-weight:700;font-size:16px;color:var(--navy)}
.client-role{left:0;width:1200px;top:258px;text-align:center;font-size:11px;color:var(--navy)}
.quote{left:340px;top:290px;width:520px;text-align:center;font-size:11.5px;line-height:1.6;color:var(--navy)}
.quote-mark{font-family:"Roboto",sans-serif;font-size:110px;color:var(--navy);opacity:.5;line-height:1}
.dots{left:560px;top:384px;display:flex;gap:10px}
.dots i{width:9px;height:9px;border-radius:50%;background:rgba(22,49,75,.35);display:block}
.dots i.on{background:var(--navy)}

/* social / subscribe */
.social{left:0;top:2840px;width:1200px;height:120px;background:var(--navy)}
.social-dot{top:48px;width:24px;height:24px;border-radius:50%;background:#9fb3c6}
.sub-input{left:700px;top:44px;width:276px;height:34px;background:#2a4a68;color:#9fb3c6;font-size:11px;line-height:34px;padding-left:12px}
.sub-btn{left:976px;top:44px;width:124px;height:34px;line-height:34px;background:var(--navy-deep);border:1px solid #456;font-size:14px;color:var(--white);font-family:"Roboto",sans-serif;text-align:center}

/* footer */
.footer{left:0;top:2960px;width:1200px;height:300px;background:var(--navy-deep);color:#b9c6d3}
.foot-brand{left:100px;top:60px;font-family:"Roboto",sans-serif;font-weight:700;color:var(--white);font-size:18px;display:flex;align-items:center;gap:10px}
.foot-brand i{width:28px;height:28px;background:var(--teal);display:block}
.foot-about{left:100px;top:110px;width:200px;font-size:12px;line-height:1.5;color:var(--white)}
.foot-phone{left:100px;top:160px;font-size:12px;color:var(--white);display:flex;align-items:center;gap:8px}
.foot-col{top:60px}
.foot-col h4{font-size:13px;font-weight:500;color:var(--white);margin-bottom:18px}
.foot-col ul{list-style:none}
.foot-col li{font-size:10px;margin-bottom:14px;letter-spacing:.4px;display:flex;align-items:center;gap:8px}
.foot-col li::before{content:"";width:5px;height:5px;border-radius:50%;background:var(--orange)}
.field{width:200px;height:24px;background:#e9eef3;margin-bottom:10px;font-size:10px;color:#7a8896;line-height:24px;padding-left:8px}
.submit{width:200px;height:24px;line-height:24px;background:var(--orange-dark);font-size:10px;font-weight:700}
.copyright{left:0;top:3260px;width:1200px;height:52px;background:var(--navy-darkest);color:#8a9aab;font-size:10px;text-align:center;line-height:52px}
</style>
</head>
<body>

<section class="hero abs">
  <div class="brand abs"><span class="brand-mark"></span>FERRO WAVE</div>
  <nav class="main-nav abs">
    <span>HOME</span>
    <span><span class="wh">WHO</span> WE ARE</span>
    <span><span class="wh">WHAT</span> WE DO</span>
    <span><span class="wh">WHEN</span> YOU NEED US</span>
    <span><span class="wh">WHERE</span> TO REACH US</span>
    <span>REGISTER DOMAIN</span>
  </nav>
  <h1 class="hero-title abs">Web Hosting Services</h1>
  <span class="btn hero-btn abs">LEARN MORE</span>
  <div class="hero-art abs" role="img" aria-label="Illustration of a desktop computer surrounded by cloud, server and settings icons"></div>
  <div class="badge abs">
    <div class="num">15</div>
    <div class="yrs">years</div>
    <div class="of">of HOSTING</div>
  </div>
</section>
<svg class="torn abs" viewBox="0 0 1200 60" preserveAspectRatio="none" aria-hidden="true">
  <path fill="#e8f5fa" d="M0 50 L40 38 L80 46 L120 30 L170 44 L210 28 L260 42 L300 32 L350 46 L400 26 L450 40 L500 30 L550 44 L600 28 L650 42 L700 30 L750 46 L800 28 L850 40 L900 30 L950 44 L1000 26 L1050 42 L1100 32 L1150 44 L1200 30 L1200 60 L0 60 Z"/>
</svg>

<section class="about abs">
  <h2 class="abs">New to Ferro Wave?</h2>
  <div class="about-copy abs">
    <p>Ferro Wave is a trusted leader in hosting and domain services for small companies and nonprofit groups. Since 2002 we have kept sites online with steady uptime, careful backups and friendly support through our long standing partners.</p>
    <p>We focus only on hosting. Your developer gets FTP access to our dedicated Linux server, and we handle the rest: monitoring, security updates, redirects for your email and plain reports so you always know how your site is doing. No design work, no surprises.</p>
    <p>Our hosting plans are simple to compare and rarely change, so budgeting is easy. Pick a plan, register a domain and let us keep the lights on while you focus on the work that matters to you.</p>
    <p>Want to know more about our plans? Visit the pricing tab or reach us any time.</p>
  </div>
  <span class="learn abs">Learn More</span>
  <div class="about-art abs" role="img" aria-label="Illustration of a laptop with charts, cloud and settings icons on a desk"></div>
</section>

<section class="domain abs">
  <div class="domain-label abs"><small>FIND YOUR</small><b>DOMAIN</b></div>
  <div class="domain-input abs"></div>
  <div class="domain-ext abs">.com</div>
  <span class="btn domain-btn abs">SEARCH</span>
</section>

<section class="services abs">
  <h2 class="section-title abs">OUR SERVICES</h2>
  <div class="svc abs" style="left:100px">
    <svg width="56" height="48" viewBox="0 0 56 48" aria-hidden="true"><rect x="4" y="4" width="48" height="30" rx="2" fill="none" stroke="#fff" stroke-width="3"/><rect x="22" y="34" width="12" height="8" fill="#fff"/><rect x="14" y="42" width="28" height="3" fill="#fff"/></svg>
    <h3>Web Hosting</h3>
    <p>Fast, steady hosting for small sites with daily backups and full FTP access.</p>
    <span class="btn">READ MORE</span>
  </div>
  <div class="svc abs" style="left:360px">
    <svg width="56" height="48" viewBox="0 0 56 48" aria-hidden="true"><path d="M14 32 a10 10 0 0 1 2-20 a13 13 0 0 1 24 2 a9 9 0 0 1 2 18 Z" fill="#fff"/><path d="M20 34 v10 M28 34 v10 M36 34 v10" stroke="#fff" stroke-width="2"/></svg>
    <h3>Cloud Hosting</h3>
    <p>Flexible cloud space that grows with your traffic and keeps pages quick.</p>
    <span class="btn">READ MORE</span>
  </div>
  <div class="svc abs" style="left:620px">
    <svg width="56" height="48" viewBox="0 0 56 48" aria-hidden="true"><rect x="16" y="2" width="24" height="12" fill="#fff"/><rect x="16" y="18" width="24" height="12" fill="#fff"/><rect x="16" y="34" width="24" height="12" fill="#fff"/><circle cx="34" cy="8" r="2" fill="#3d8fd3"/><circle cx="34" cy="24" r="2" fill="#3d8fd3"/><circle cx="34" cy="40" r="2" fill="#3d8fd3"/></svg>
    <h3>Dedicated hosting</h3>
    <p>Your own space on our dedicated Linux server for busy, growing sites.</p>
    <span class="btn">READ MORE</span>
  </div>
  <div class="svc abs" style="left:880px">
    <svg width="56" height="48" viewBox="0 0 56 48" aria-hidden="true"><ellipse cx="24" cy="10" rx="16" ry="6" fill="#fff"/><path d="M8 10 v26 a16 6 0 0 0 32 0 v-26" fill="none" stroke="#fff" stroke-width="3"/><path d="M8 22 a16 6 0 0 0 32 0" fill="none" stroke="#fff" stroke-width="3"/><circle cx="44" cy="36" r="9" fill="#fff"/><path d="M40 36 l3 3 l5 -6" stroke="#3d8fd3" stroke-width="2.5" fill="none"/></svg>
    <h3>Data Protection</h3>
    <p>Secure storage, regular backups and monitoring that guard your data.</p>
    <span class="btn">READ MORE</span>
  </div>
</section>

<section class="prices abs">
  <h2 class="section-title abs">PRICES</h2>
  <p class="prices-sub abs">Simple plans for small companies and nonprofits with no hidden costs. Choose the plan that fits your site and upgrade at any time as you grow.</p>

  <div class="plan beginner abs" style="left:88px">
    <div class="plan-head"><h3>BEGINNER</h3><p>30 days free trial</p></div>
    <ul><li>24/7 TECH SUPPORT</li><li>ADVANCED OPTIONS</li><li>10GB STORAGE</li><li>1GB BANDWIDTH</li><li>EVERYTHING IS IN</li><li>ANOTHER FEATURE HERE</li></ul>
    <span class="btn">ORDER NOW</span>
  </div>
  <div class="plan standard abs" style="left:444px">
    <div class="plan-head"><h3>STANDARD</h3><p>30 days free trial</p></div>
    <ul><li>24/7 TECH SUPPORT</li><li>ADVANCED OPTIONS</li><li>10GB STORAGE</li><li>1GB BANDWIDTH</li><li>EVERYTHING IS IN</li><li>ANOTHER FEATURE HERE</li></ul>
    <span class="btn">ORDER NOW</span>
  </div>
  <div class="plan establishment abs" style="left:800px">
    <div class="plan-head"><h3>ESTABLISHMENT</h3><p>30 days free trial</p></div>
    <ul><li>24/7 TECH SUPPORT</li><li>ADVANCED OPTIONS</li><li>10GB STORAGE</li><li>1GB BANDWIDTH</li><li>EVERYTHING IS IN</li><li>ANOTHER FEATURE HERE</li></ul>
    <span class="btn">ORDER NOW</span>
  </div>
</section>

<section class="clients abs" role="img" aria-label="Warm orange city skyline backdrop behind client testimonial">
  <h2 class="section-title abs">WHAT CLIENTS THINK</h2>
  <div class="avatar abs" role="img" aria-label="Client portrait photo"></div>
  <div class="client-name abs">John Doe</div>
  <div class="client-role abs">Director</div>
  <div class="abs quote-mark" style="left:250px;top:270px">“</div>
  <p class="quote abs">Ferro Wave has hosted our site for years without a single outage we noticed. Support is quick, the pricing is clear, and our developer loves the simple FTP setup on their server.</p>
  <div class="abs quote-mark" style="left:880px;top:270px">”</div>
  <div class="dots abs"><i class="on"></i><i></i><i></i></div>
</section>

<section class="social abs">
  <span class="social-dot abs" style="left:134px" aria-label="Social profile"></span>
  <span class="social-dot abs" style="left:232px" aria-label="Social profile"></span>
  <span class="social-dot abs" style="left:340px" aria-label="Social profile"></span>
  <span class="social-dot abs" style="left:446px" aria-label="Social profile"></span>
  <div class="sub-input abs">Enter your email address</div>
  <div class="sub-btn abs">Subscribe</div>
</section>

<footer class="footer abs">
  <div class="foot-brand abs"><i></i>FERRO WAVE</div>
  <p class="foot-about abs">It is a long established fact that a reader will be distracted by.</p>
  <div class="foot-phone abs">
    <svg width="14" height="14" viewBox="0 0 24 24" aria-hidden="true"><path fill="#f6a623" d="M6.6 10.8a15 15 0 0 0 6.6 6.6l2.2-2.2c.3-.3.7-.4 1-.2 1.1.4 2.3.6 3.6.6.6 0 1 .4 1 1V20c0 .6-.4 1-1 1A17 17 0 0 1 3 4c0-.6.4-1 1-1h3.5c.6 0 1 .4 1 1 0 1.3.2 2.5.6 3.6.1.3 0 .7-.2 1z"/></svg>
    888.514.2973
  </div>
  <div class="foot-col abs" style="left:380px">
    <h4>Quick Links</h4>
    <ul><li>WHO WE ARE</li><li>WHAT WE DO</li><li>WHEN YOU NEED US</li><li>WHERE TO REACH US</li><li>REGISTER DOMAIN</li><li>PRIVACY POLICY</li></ul>
  </div>
  <div class="foot-col abs" style="left:600px">
    <h4>Services</h4>
    <ul><li>WEB HOSTING</li><li>CLOUD HOSTING</li><li>DEDICATED HOSTING</li><li>DATA PROTECTION</li></ul>
  </div>
  <div class="foot-col abs" style="left:840px">
    <h4>Contact Us</h4>
    <div class="field">Name</div>
    <div class="field">Email</div>
    <div class="field">Message</div>
    <span class="btn submit">SUBMIT</span>
  </div>
</footer>
<div class="copyright abs">ferrowave.com © 2017. All rights reserved.</div>

</body>
</html>
```